Supplement Package and Bottle Design*

We are a supplement company rebranding a number of product ranges for which we need a designer.

We will start with two products for joint health supplementation that are part of one range.

1. QUENTIL R58 Internal Oil Drops
The internal oil drop requires a design for the outer box and inside bottle label – see attached.

Front of box should include the following text:
- QUENTIL R58
- Internal Oil Drops
- Original formula from the oils of fresh Laurus nobilis L. leaves and Curcuma longa L. rhizomes
- Dilute before use
- Food supplement
- 100ml
- Some prominent icon/ graphics indicating use for joint health
- Brenuvel logo

2. QUENTIL M4 External Cream
The external cream only requires a design for the bottle label – see attached.
- QUENTIL M4
- External Cream
- Original formula from the oils of fresh Laurus nobilis L. leaves + 7 select ingredients
- 150ml
- Brenuvel logo

Overall design:
- Common design between both products (oil drops and cream)
Must appeal to a customer base of middle-age/ seniors
- Pharmaceutical product feel with touch of nature/ herbal remedy
- Design my convey a feeling of dependability, trust, effectiveness
- Premium product feel. These are very expensive products
- Design must be easy to adapt for new product ranges
- Use icons/ symbols to indicate health application, example: icon of knee to indicate use for joints
- "R58" and "M4" should be prominent to distinguish the products
- You have a choice of two Brenuvel logos. See attached.
- Primary colours: white and rgb(33, 136, 135)
- Designers can also consider some use of stamped gold/ silver for embellishments

Once a successful design/ feel has been chosen then exact dielines will be provided.

Target Market(s)

Seniors (65+ years old) with arthritis. Generally retired and affluent.

Industry/Entity Type

Health Product

Colors
33b8a4

Requirements
Must have
• As per project description.

Please creatively use a laurel wreath in the design. Either as a standalone element or multiple laurel wreaths in the background of the design. Can be vector or blended image.

As the supplements are made from bay leaves (laurel leaves) this subtle connection should be present.
Should not have
• Should not be cheap design and loud.

Premium design that conveys trust and pharmaceutical grade treatment with embellishments reminding that this is a natural/ herbal remedy product

```html
<!DOCTYPE html>
<html lang="en">
<head>
<meta charset="utf-8">
<title>QUENTIL R58 Internal Oil Drops – Bottle Label</title>
<link rel="stylesheet" href="https://fonts.googleapis.com/css2?family=Libre+Baskerville&family=Montserrat:wght@400;500;600&display=swap">
<style>
  :root {
    --stage: #e4e6ea;
    --teal: #218887;
    --teal-light: #2e9a98;
    --teal-dark: #17706f;
    --white: #ffffff;
    --band: #f3f4f4;
    --ink-soft: #a9d6d4;
    --photo-light: #e9e9e9;
    --photo-mid: #b9b9b9;
    --photo-accent: #e8a0a0;
  }
  * { margin: 0; padding: 0; box-sizing: border-box; }
  html, body {
    width: 1200px; height: 900px; overflow: hidden;
    background: var(--stage);
  }
  .canvas {
    width: 1200px; height: 900px;
    display: flex; align-items: center; justify-content: center;
  }
  .label {
    position: relative;
    width: 460px; height: 840px;
    background: linear-gradient(90deg, var(--teal-dark) 0%, var(--teal-light) 35%, var(--teal) 70%, var(--teal-dark) 100%);
    overflow: hidden;
    font-family: "Montserrat", sans-serif;
    color: var(--white);
  }
  .brand-top {
    position: absolute; top: 52px; left: 0; right: 0;
    display: flex; flex-direction: column; align-items: center; gap: 12px;
  }
  .brand-top .mark {
    width: 96px; height: 96px; border-radius: 50%;
    border: 3px solid var(--ink-soft);
  }
  .brand-top .name {
    font-size: 17px; letter-spacing: 5px; font-weight: 500; color: var(--ink-soft);
  }
  .joint-photo {
    position: absolute; top: 220px; left: 12px;
    width: 196px; height: 196px; border-radius: 50%;
    background: radial-gradient(circle at 45% 60%, var(--photo-accent) 0%, var(--photo-light) 35%, var(--photo-mid) 100%);
  }
  .product {
    position: absolute; top: 222px; left: 226px; right: 14px;
    text-align: right;
  }
  .product .range {
    font-family: "Libre Baskerville", serif;
    font-size: 32px; line-height: 1; letter-spacing: 0.5px;
  }
  .product .code {
    font-family: "Libre Baskerville", serif;
    font-size: 100px; line-height: 1.05; letter-spacing: -2px;
  }
  .product .form {
    font-size: 25px; font-weight: 500; margin-top: 6px; white-space: nowrap;
  }
  .product .formula {
    font-size: 12.5px; line-height: 1.45; margin-top: 12px;
    color: var(--ink-soft); text-align: left;
  }
  .caption {
    position: absolute; left: 0; right: 0;
    text-align: center; font-weight: 600; letter-spacing: 5px;
  }
  .caption.supplement { top: 520px; font-size: 17px; }
  .caption.dilute { top: 718px; font-size: 17px; }
  .caption.volume { top: 770px; font-size: 32px; font-weight: 500; letter-spacing: 6px; }
  .brand-band {
    position: absolute; top: 552px; left: 0; right: 0; height: 150px;
    background: linear-gradient(90deg, #dfe2e2 0%, var(--white) 35%, var(--band) 75%, #dfe2e2 100%);
    display: flex; flex-direction: column; align-items: center; justify-content: center; gap: 14px;
  }
  .brand-band .mark {
    width: 72px; height: 72px; border-radius: 50%;
    border: 3px solid var(--teal);
  }
  .brand-band .name {
    font-size: 22px; letter-spacing: 6px; font-weight: 500; color: var(--teal);
  }
</style>
</head>
<body>
<main class="canvas">
  <section class="label">
    <div class="brand-top">
      <span class="mark"></span>
      <span class="name">BRENUVEL</span>
    </div>

    <div class="joint-photo" role="img" aria-label="Black and white photo of hands holding a painful knee, highlighted in red"></div>

    <div class="product">
      <p class="range">QUENTIL</p>
      <p class="code">R58</p>
      <p class="form">Internal Oil Drops</p>
      <p class="formula">Original formula from the oils of fresh Laurus nobilis L. leaves and Curcuma longa L. rhizomes</p>
    </div>

    <p class="caption supplement">FOOD SUPPLEMENT</p>

    <div class="brand-band">
      <span class="mark"></span>
      <span class="name">BRENUVEL</span>
    </div>

    <p class="caption dilute">DILUTE BEFORE USE</p>
    <p class="caption volume">100ml</p>
  </section>
</main>
</body>
</html>
```